Torven Medical needs bold attention catching website for healthcare professionals(target)

I need a hero page as well as a products and about page for a website of mine. I specialize in orthopedic instruments . Specifically bone drills and saws. This whole company was founded to bring superb quality highly discounted medical instruments. Specifically bone drills, bone saws, k-wires and pins. Two main points should be cost savings and superior quality.

Target Market(s)

healthcare professionals Surgeons and hospital material managers

Number of Pages Required

3 page

Font styles to use
Serif

Colors

Designer to choose colors to be used in the design.

Requirements
Must have
• colors should match logo design

```html
<!DOCTYPE html>
<html lang="en">
<head>
<meta charset="utf-8">
<title>Torven Medical — Orthopaedic Instruments</title>
<link href="https://fonts.googleapis.com/css2?family=Poppins:wght@300;400;500;600;700&display=swap" rel="stylesheet">
<style>
:root{
  --orange:#f7901e;
  --orange-deep:#e07c12;
  --brown:#7a4a1e;
  --ink:#1e1e1e;
  --grey:#8a8a8a;
  --line:#e6e6e6;
  --white:#ffffff;
  --cream:#fdf6ef;
}
*{box-sizing:border-box;margin:0;padding:0}
html,body{width:1200px;height:2703px;overflow:hidden}
body{position:relative;font-family:'Poppins',sans-serif;color:var(--ink);background:var(--white)}
.abs{position:absolute}

/* hero */
.hero-art{position:absolute;left:0;top:0;width:1200px;height:600px}
.nav{position:absolute;top:36px;left:0;width:1200px;height:26px}
.brand{position:absolute;left:136px;top:-2px;font-size:18px;font-weight:500;color:var(--ink);display:flex;align-items:center;gap:8px}
.brand .dot{width:12px;height:12px;border-radius:50%;background:var(--orange)}
.menu{position:absolute;top:6px;font-size:9.5px;color:#3a3a3a}
.menu.active{color:var(--orange)}
.btn{position:absolute;display:flex;align-items:center;justify-content:center;border-radius:16px;font-size:9.5px;font-weight:600}
.btn-orange{background:var(--orange);color:var(--ink)}
.hero-title{position:absolute;left:194px;top:214px;width:460px;font-size:28px;line-height:31px;color:var(--white);font-weight:400}
.btn-ghost{border:1px solid var(--white);color:var(--white)}

/* about */
.about-title{position:absolute;left:313px;top:634px;font-size:13px}
.about-title b{font-weight:600}
.about-title span{color:var(--orange)}
.about-text{position:absolute;left:313px;top:670px;width:575px;font-size:13.3px;line-height:19px;color:var(--grey);text-align:justify;font-weight:300}
.link{position:absolute;font-size:9.5px;color:var(--orange)}

/* products */
.eyebrow{position:absolute;font-size:8.5px;letter-spacing:2.2px;font-weight:600;color:var(--orange)}
.products-heading{position:absolute;left:75px;top:1010px;width:290px;font-size:21px;line-height:28px}
.card{position:absolute;top:891px;width:218px;height:324px;border:1px solid var(--line);border-radius:6px;background:var(--white)}
.card-photo{position:absolute;left:0;top:0;width:216px;height:186px;border-radius:6px 6px 0 0}
.card h3{position:absolute;left:24px;top:209px;font-size:12px;font-weight:400}
.card p{position:absolute;left:24px;top:233px;width:170px;font-size:8.8px;line-height:15px;color:var(--grey)}
.card .go{position:absolute;left:24px;top:302px;width:31px;height:31px;border:1px solid var(--orange);border-radius:50%;background:var(--white);display:flex;align-items:center;justify-content:center}

/* why band */
.why{position:absolute;left:0;top:1299px;width:1200px;height:304px;background:var(--orange)}
.why .eyebrow{left:0;width:1200px;text_align:center;text-align:center;top:74px;color:var(--ink)}
.feature{position:absolute;top:120px;width:170px}
.feature svg{display:block;height:18px}
.feature h4{margin-top:10px;font-size:13px;line-height:19px;font-weight:500;color:var(--ink)}
.feature p{margin-top:12px;font-size:8.8px;line-height:15px;color:#9c4f05}

/* updates */
.updates-title{position:absolute;left:0;width:1200px;top:1670px;text-align:center;font-size:20px}
.blog-photo{position:absolute;left:194px;top:1722px;width:378px;height:313px}
.blog-tag{position:absolute;left:225px;top:1742px;font-size:8.5px;letter-spacing:2px;color:var(--white);font-weight:600}
.blog-card{position:absolute;left:194px;top:1910px;width:277px;height:125px;background:var(--white)}
.blog-card .meta{position:absolute;left:31px;top:30px;font-size:8px;color:#555}
.blog-card h4{position:absolute;left:31px;top:52px;width:190px;font-size:10.5px;line-height:16px;font-weight:400}
.press-item{position:absolute;left:630px;width:377px;border-top:1px solid var(--line)}
.press-item p{margin-top:14px;font-size:9px;line-height:15px;width:330px}
.press-item span{display:block;margin-top:6px;font-size:7.5px;letter-spacing:.5px;color:var(--orange-deep)}

/* quote */
.quote-title{position:absolute;left:0;width:1200px;top:2290px;text-align:center;font-size:26px;font-weight:600;color:var(--white)}
.quote-sub{position:absolute;left:0;width:1200px;top:2326px;text-align:center;font-size:9px;color:var(--white)}
.field{position:absolute;background:var(--white);border-radius:16px;font-size:8.5px;color:#aaa;padding:11px 17px}
.social{position:absolute;left:1023px;width:31px;height:31px;border-radius:50%;border:1px solid rgba(255,255,255,.35);background:rgba(255,255,255,.08)}
.call{position:absolute;left:0;width:1200px;top:2628px;text-align:center;font-size:20px;color:#2a1a0a}
.call b{font-weight:500}
.mail{position:absolute;left:0;width:1200px;top:2656px;text-align:center;font-size:8.5px;color:#2a1a0a}
.foot{position:absolute;top:2646px;font-size:8.5px;color:#2a1a0a}
</style>
</head>
<body>

<!-- hero -->
<svg class="hero-art" viewBox="0 0 1200 600" role="img" aria-label="Photo of surgeons in an operating room with three surgical power tools, tinted teal to orange">
  <defs>
    <linearGradient id="heroTint" x1="0" y1="1" x2="1" y2="0">
      <stop offset="0" stop-color="#2e7f78"/>
      <stop offset=".35" stop-color="#8fa06a"/>
      <stop offset=".6" stop-color="#e2a060"/>
      <stop offset="1" stop-color="#f0ad6a"/>
    </linearGradient>
  </defs>
  <path d="M0 0H1200V500C1100 420 980 420 880 470C760 530 680 565 560 562C420 558 330 470 230 420C150 380 60 370 0 378Z" fill="url(#heroTint)"/>
  <rect x="790" y="120" width="320" height="360" fill="#ffffff" opacity=".18" rx="40"/>
</svg>

<nav class="nav">
  <div class="brand"><span class="dot"></span>Torven Medical</div>
  <span class="menu active" style="left:418px">Home</span>
  <span class="menu" style="left:473px">Company</span>
  <span class="menu" style="left:546px">Products</span>
  <span class="menu" style="left:617px">Services</span>
  <span class="menu" style="left:683px">Blog</span>
  <span class="menu" style="left:734px">Contact</span>
  <span class="menu" style="left:802px">Call. &nbsp;☏ &nbsp;+ 1 800 555 01 42</span>
  <span class="btn btn-orange" style="left:952px;top:0;width:113px;height:25px">Request A Quote</span>
</nav>

<h1 class="hero-title">Lorem ipsum dolor sit amet, consectetur adipiscing elit, sed do eiusmod tempor.</h1>
<span class="btn btn-orange" style="left:194px;top:341px;width:100px;height:30px">Contact Us</span>
<span class="btn btn-ghost" style="left:306px;top:341px;width:75px;height:30px">More</span>

<!-- about -->
<svg class="abs" style="left:1070px;top:610px" width="130" height="260" aria-hidden="true">
  <circle cx="27" cy="26" r="18" fill="var(--cream)"/>
  <circle cx="150" cy="130" r="110" fill="var(--cream)" opacity=".6"/>
</svg>
<h2 class="about-title"><b>Torven</b> <span>Medical</span> Specialize in orthopaedic instruments</h2>
<p class="about-text">Lorem ipsum dolor sit amet, consectetur adipiscing elit, sed do eiusmod tempor incididunt ut labore et dolore magna aliqua. Ut enim ad minim veniam, quis nostrud exercitation ullamco laboris nisi ut aliquip ex ea commodo consequat. Duis aute irure dolor in reprehenderit in voluptate velit esse cillum dolore eu fugiat nulla pariatur. Excepteur sint occaecat cupidatat non proident, sunt in culpa qui officia deserunt mollit anim id est laborum.</p>
<span class="link" style="left:313px;top:806px">Our Company &nbsp;→</span>

<!-- products -->
<svg class="abs" style="left:0;top:890px" width="200" height="410" aria-hidden="true">
  <path d="M0 10C60 0 100 60 90 150C80 250 40 320 200 410H0Z" fill="var(--cream)" opacity=".7"/>
</svg>
<span class="eyebrow" style="left:75px;top:989px">OUR PRODUCTS</span>
<h2 class="products-heading">Duis aute irure dolor in repre-henderit in voluptate velit esse cillum dolore eu fugiat nulla pariatur</h2>

<article class="card" style="left:431px">
  <div class="card-photo" role="img" aria-label="Photo of cordless bone drills with chucks" style="background:linear-gradient(135deg,#f4f4f4,#b8b8b8 60%,#2a2a2a)"></div>
  <h3>Bone Drills</h3>
  <p>Torven is better way to get the hands-on financial advising services you need to be successful.</p>
  <span class="go"><svg width="10" height="10" viewBox="0 0 10 10"><path d="M1 5H9M6 2L9 5 6 8" stroke="var(--orange)" fill="none"/></svg></span>
</article>
<article class="card" style="left:668px">
  <div class="card-photo" role="img" aria-label="Photo of sagittal bone saw blades" style="background:linear-gradient(135deg,#f4f4f4,#d2d2d2 55%,#9a9a9a)"></div>
  <h3>Bone Saws</h3>
  <p>Torven lets you visualize your finances in real-time from the convenience of your mobile device.</p>
  <span class="go"><svg width="10" height="10" viewBox="0 0 10 10"><path d="M1 5H9M6 2L9 5 6 8" stroke="var(--orange)" fill="none"/></svg></span>
</article>
<article class="card" style="left:906px">
  <div class="card-photo" role="img" aria-label="Photo of k-wires and threaded pins" style="background:linear-gradient(135deg,#f6f6f6,#c9cbcc 60%,#5d6163)"></div>
  <h3>k-wires &amp; Pins</h3>
  <p>Torven lets you visualize your finances in real-time from the convenience of your mobile device.</p>
  <span class="go"><svg width="10" height="10" viewBox="0 0 10 10"><path d="M1 5H9M6 2L9 5 6 8" stroke="var(--orange)" fill="none"/></svg></span>
</article>

<!-- why -->
<section class="why">
  <span class="eyebrow">WHY TORVEN MEDICAL</span>
  <div class="feature" style="left:313px">
    <svg viewBox="0 0 18 18" width="18"><path d="M1 8H4V17H1ZM5 8L9 2C11 2 11 4 10 7H16C17 7 17.5 8 17 9L15 16C14.7 17 14 17 13 17H5Z" fill="var(--ink)"/></svg>
    <h4>Quality Assurance<br>and Testing</h4>
    <p>Duis aute irure dolor in reprehen-derit in voluptate esse cillum dolore eu fugiat nulla</p>
  </div>
  <div class="feature" style="left:520px">
    <svg viewBox="0 0 18 18" width="18"><circle cx="9" cy="9" r="4" fill="var(--ink)"/><path d="M9 1V3M9 15V17M1 9H3M15 9H17M3.5 3.5L5 5M13 13L14.5 14.5M3.5 14.5L5 13M13 5L14.5 3.5" stroke="var(--ink)" stroke-width="1.6"/></svg>
    <h4>Highly Focused R&amp;D<br>&amp; innovation</h4>
    <p>Duis aute irure dolor in reprehen-derit in voluptate esse cillum dolore eu fugiat nulla</p>
  </div>
  <div class="feature" style="left:728px">
    <svg viewBox="0 0 12 18" width="12"><text x="0" y="15" font-family="Poppins,sans-serif" font-size="17" font-weight="600" fill="#1e1e1e">$</text></svg>
    <h4>Best Competitive<br>Pricing</h4>
    <p>Duis aute irure dolor in reprehen-derit in voluptate esse cillum dolore eu fugiat nulla</p>
  </div>
</section>

<!-- updates -->
<h2 class="updates-title">Latest Updates</h2>
<div class="blog-photo" role="img" aria-label="Photo of a field medic crouching with children outdoors" style="background:linear-gradient(120deg,#6f6a60,#b5ab98 50%,#5c5346)"></div>
<span class="blog-tag">BLOG POST</span>
<svg class="abs" style="left:513px;top:1743px" width="30" height="8" aria-hidden="true">
  <circle cx="4" cy="4" r="3" fill="#fff"/><circle cx="14" cy="4" r="3" fill="none" stroke="#fff"/><circle cx="24" cy="4" r="3" fill="none" stroke="#fff"/>
</svg>
<div class="blog-card">
  <span class="meta">Apr 2 2019 &nbsp;I&nbsp; By Admin</span>
  <h4>7 Ways to Bring Hope and Spread Kindness this National Month of Hope</h4>
</div>

<span class="eyebrow" style="left:630px;top:1741px;font-size:8px">PRESS RELEASE</span>
<div class="press-item" style="top:1766px"><p>Lorem ipsum dolor sit amet, consectetur adipiscing elit, sed do eiusmod tempor incididunt ut labore et dolore magna aliqua</p><span>JUN 26 2019</span></div>
<div class="press-item" style="top:1842px"><p>Lorem ipsum dolor sit amet, consectetur adipiscing elit, sed do eiusmod tempor incididunt ut labore et dolore magna aliqua</p><span>JUN 26 2019</span></div>
<div class="press-item" style="top:1918px"><p>Lorem ipsum dolor sit amet, consectetur adipiscing elit, sed do eiusmod tempor incididunt ut labore et dolore magna aliqua</p><span>JUN 26 2019</span></div>
<div class="press-item" style="top:1992px;height:1px"></div>
<span class="link" style="left:630px;top:2008px;font-size:9px">Explore All &nbsp;→</span>

<!-- quote / footer -->
<svg class="abs" style="left:0;top:2100px" width="1200" height="603" viewBox="0 0 1200 603" aria-hidden="true">
  <defs>
    <linearGradient id="footFill" x1="0" y1="0" x2="1" y2="0">
      <stop offset="0" stop-color="#7a4a1e"/>
      <stop offset=".55" stop-color="#c9741c"/>
      <stop offset="1" stop-color="#e88e2a"/>
    </linearGradient>
  </defs>
  <path d="M0 40C80 70 150 130 300 110C470 90 560 20 760 10C920 0 1050 30 1200 110V603H0Z" fill="url(#footFill)"/>
  <path d="M0 170C120 260 160 420 260 603H0Z" fill="#6a3e18" opacity=".35"/>
  <path d="M1200 180C1060 190 900 280 940 400C980 520 1120 560 1200 603Z" fill="#f29a3a" opacity=".35"/>
</svg>

<h2 class="quote-title">Get A Quick Quote</h2>
<p class="quote-sub">Duis aute irure dolor in reprehenderit in voluptate velit esse cillum dolore eu fugiat nulla.</p>
<div class="field" style="left:313px;top:2367px;width:277px;height:31px">Enter your Name</div>
<div class="field" style="left:609px;top:2367px;width:278px;height:31px">Email</div>
<div class="field" style="left:313px;top:2417px;width:277px;height:31px">Phone</div>
<div class="field" style="left:609px;top:2417px;width:278px;height:31px">Subject</div>
<div class="field" style="left:313px;top:2467px;width:574px;height:75px;border-radius:12px">Message ...</div>
<span class="btn btn-orange" style="left:532px;top:2567px;width:136px;height:31px">Request A Quote</span>

<span class="social" style="top:2296px" aria-label="Social link"></span>
<span class="social" style="top:2338px" aria-label="Social link"></span>
<span class="social" style="top:2379px" aria-label="Social link"></span>
<span class="social" style="top:2420px" aria-label="Social link"></span>

<span class="foot" style="left:134px">© 2019 by Torven Medical</span>
<p class="call">Call. <b>+ 1 800 555 0142</b></p>
<p class="mail">E. info@torvenmedical.com</p>
<span class="foot" style="left:914px">Home &nbsp;&nbsp; I &nbsp;&nbsp; Company &nbsp;&nbsp; I &nbsp;&nbsp; Contact</span>

</body>
</html>
```